Litigation services brochure for PRV.law

improve aesthetics and sync with website color scheme and new staff to emphasize law firm's litigation capabilities. Describe Litigation director, senior attorneys, attorneys, and general capabilities of the firm, licenses to practice, representative trasnactions and litigation experience. Take profile info from individual attorneys listed in the .doc and correlate with www.prv.law profiles for same attorneys. Update photos as needed. I'm not sure what other words I need to add, but this thing says there needs to be more words in my project description. read the brochure attached, and it should be pretty self explanatory. We have lots of info and content on there, we just want it to look better and reflect the updated color scheme of the site (a few of the color bar colors have changed order and color).

Target Market(s)

Houston, Denver

Font styles to use
Serif

Requirements
Must have
• Color scheme that matches www.prv.law
Nice to have
• Better aesthetics and content optimization

```html
<!DOCTYPE html>
<html lang="en">
<head>
<meta charset="utf-8">
<title>PRV.law Litigation Brochure</title>
<link href="https://fonts.googleapis.com/css2?family=PT+Sans+Narrow:wght@400;700&family=Tinos:ital@0;1&display=swap" rel="stylesheet">
<style>
  :root {
    --stage: #141414;
    --page-left: #333132;
    --page-right: #363435;
    --placeholder: #4a4849;
    --text: #e6e4e4;
    --muted: #c9c7c7;
    --heading-grey: #75737a;
    --cell: #4d4b4c;
    --rule: #5a5859;
    --gold: #e9b21c;
    --orange: #e67e22;
    --accent-rule: #c98f2a;
  }
  * { box-sizing: border-box; margin: 0; padding: 0; }
  html, body { width: 1200px; height: 1200px; overflow: hidden; }
  body {
    background: var(--stage);
    font-family: "PT Sans Narrow", "Arial Narrow", sans-serif;
    color: var(--text);
    position: relative;
  }
  .spread { position: absolute; width: 758px; height: 491px; display: flex; }
  .spread--fees { left: 78px; top: 68px; }
  .spread--team { left: 300px; top: 627px; }
  .page { position: relative; width: 50%; height: 100%; background: var(--page-left); overflow: hidden; }
  .page--right {
    background: linear-gradient(90deg, #2a292a 0, #3a3839 14px, var(--page-right) 30px);
  }

  .library-backdrop {
    position: absolute; left: 0; right: 0; bottom: 0; height: 360px;
    background:
      radial-gradient(ellipse at 78% 70%, rgba(120,118,118,.35), transparent 60%),
      linear-gradient(180deg, rgba(0,0,0,0) 0, rgba(70,68,69,.55) 45%, rgba(40,39,40,.85) 100%);
    pointer-events: none;
  }

  .profile { position: absolute; left: 34px; width: 313px; font-size: 6.4px; line-height: 8.1px; }
  .profile__photo {
    float: left; width: 74px; height: 74px; margin: 0 13px 4px 0;
    background: var(--placeholder);
  }
  .profile__photo--portrait { background: linear-gradient(160deg, #cfcfcf 0%, #8d8d8d 45%, #2e2e2e 100%); }
  .profile__head {
    display: flow-root; border-bottom: 0.8px solid var(--accent-rule);
    padding-bottom: 5px; margin-bottom: 8px;
  }
  .profile__name { font-weight: 700; font-size: 7.4px; line-height: 9px; }
  .profile__title { font-weight: 700; font-size: 5px; line-height: 7px; }
  .profile__contact { font-size: 5px; line-height: 6px; }
  .profile__bio p { text-align: justify; margin-bottom: 8px; color: var(--muted); }
  .admissions { clear: both; padding-top: 8px; }
  .admissions__title { font-weight: 700; font-size: 6.8px; margin-bottom: 9px; }
  .admissions li { list-style: none; color: var(--muted); }

  .fee-title {
    position: absolute; left: 43px; top: 42px;
    font-family: "Tinos", "Times New Roman", serif;
    font-size: 21px; line-height: 21.5px; color: var(--heading-grey); letter-spacing: .3px;
  }
  .fee-section { position: absolute; left: 43px; width: 330px; }
  .fee-section__title { font-weight: 700; font-size: 8px; line-height: 8.6px; }
  .fee-section__title--orange { color: var(--orange); font-weight: 400; }
  .fee-section__title--gold { color: var(--gold); }
  .fee-section__sub { font-size: 6px; color: var(--muted); }
  .rate-table { position: absolute; border-collapse: collapse; font-size: 6.4px; }
  .rate-table th {
    background: var(--cell); font-weight: 700; height: 12.5px; padding: 0;
    border-right: 7px solid var(--page-right);
  }
  .rate-table td { height: 12.8px; padding: 0; border-bottom: 0.7px solid var(--rule); border-right: 7px solid var(--page-right); }
  .rate-table td.years { text-align: center; font-weight: 700; width: 82px; }
  .rate-table td.rate { padding-left: 4px; width: 60px; }
  .staff-table { position: absolute; left: 214px; border-collapse: collapse; font-size: 6.4px; }
  .staff-table th { background: var(--cell); height: 12.5px; }
  .staff-table td { height: 18px; border-bottom: 0.7px solid var(--rule); padding: 0; }
  .staff-table td.role { font-weight: 700; width: 54px; }
  .staff-table td.rate { padding-left: 5px; width: 60px; }
  .footnote {
    position: absolute; left: 212px; top: 430px;
    font-family: "Tinos", "Times New Roman", serif; font-style: italic;
    font-size: 4.8px; line-height: 8px; color: var(--muted);
  }

  .firm-name {
    position: absolute; left: 32px; top: 392px;
    font-size: 22px; line-height: 22px; color: #5e5c5d; letter-spacing: .5px;
  }
</style>
</head>
<body>

<section class="spread spread--fees">
  <article class="page page--left">
    <div class="profile" style="top:42px">
      <div class="profile__photo" role="img" aria-label="Attorney portrait placeholder"></div>
      <header class="profile__head">
        <p class="profile__name">Jonah R. Vance III,</p>
        <p class="profile__title">J.D., Ph.D., Managing Member, Attorney</p>
        <p class="profile__contact">E : jvance@prv.law &nbsp;&nbsp; (713) 555-0142 x104</p>
      </header>
      <div class="profile__bio">
        <p>Representing a broad range of business clients, Jonah practices intellectual property law, residential &amp; commercial property law, commercial transactions, and litigation. He advises clients on business problems and solutions, entity design and creation, mergers and acquisitions, reorganizations, dispute resolution, and strategy. He is also heavily focused on intellectual property creation and protection, filing and obtaining hundreds of trademarks, domestic and internationally. Jonah was President of the Intellectual Property &amp; Technology Law Society, President of the Alternative Dispute Resolution Advocates, and was a member and coach of Bayou State College of Law's prestigious advocacy programs. Jonah also created and manages his own advertising implementation and optimization company. Jonah is licensed in all courts and federal districts of Texas and the U.S. Tax Court. He is based in the Houston, Texas, office.</p>
      </div>
      <div class="admissions">
        <p class="admissions__title">ADMISSIONS TO PRACTICE</p>
        <ul><li>Texas</li><li>U.S. Southern, Eastern, Northern, &amp; Western Districts of Texas</li><li>US. Tax Court</li></ul>
      </div>
    </div>

    <div class="profile" style="top:258px">
      <div class="profile__photo profile__photo--portrait" role="img" aria-label="Black and white portrait of attorney in suit"></div>
      <header class="profile__head">
        <p class="profile__name">Trent L. Marlow,</p>
        <p class="profile__title">J.D., Senior Attorney, Business &amp; Litigation</p>
        <p class="profile__contact">E : tmarlow@prv.law &nbsp;(713) 555-0142 x108</p>
      </header>
      <div class="profile__bio">
        <p>Trent Lee Marlow is a Senior Attorney with Pierce, Ravel &amp; Vance, PLLC. Trent's practice focuses on construction litigation, and construction related disputes including residential &amp; commercial property law. In addition, he practices business &amp; corporate law, commercial transactions, litigation, complex business solutions, including entity creation, mergers, acquisitions, and reorganizations, as well as corporate strategy. Prior to joining Pierce, Ravel &amp; Vance, Mr. Marlow was a partner with Delacroix &amp; Marlow focusing on construction, residential &amp; commercial property, and commercial transactions.</p>
        <p>Trent completed his J.D. from Bayou State College of Law in 2011 and graduated from Gulf Coast University in 2005. Prior to working as an attorney, Trent spent several years working in the construction industry, primarily in residential and commercial construction. Trent is licensed to practice law in Texas and in the United States District Court for the Southern &amp; Eastern Districts of Texas. He is based in the Houston, Texas, office for Pierce, Ravel &amp; Vance, PLLC</p>
      </div>
      <div class="admissions">
        <p class="admissions__title">ADMISSIONS TO PRACTICE</p>
        <ul><li>Texas</li><li>U.S. Eastern &amp; Southern Districts of Texas</li></ul>
      </div>
    </div>
  </article>

  <article class="page page--right">
    <h1 class="fee-title">FEE<br>SCHEDULE*</h1>

    <div class="fee-section" style="top:121px">
      <h2 class="fee-section__title fee-section__title--orange">Oil &amp; Gas Title Matters</h2>
      <p class="fee-section__sub">Attorneys (based on years of experience)</p>
    </div>
    <table class="rate-table" style="left:43px;top:146px">
      <tr><th>Years of Experience</th><th>Rate</th></tr>
      <tr><td class="years">0-1</td><td class="rate">$150.00 - $160.00</td></tr>
      <tr><td class="years">1-2</td><td class="rate">$160.00 - $180.00</td></tr>
      <tr><td class="years">2-3</td><td class="rate">$180.00 - $200.00</td></tr>
      <tr><td class="years">3-5</td><td class="rate">$200.00 - $215.00</td></tr>
      <tr><td class="years">5-7</td><td class="rate">$215.00 - $225.00</td></tr>
      <tr><td class="years">7-10</td><td class="rate">$225.00 - $250.00</td></tr>
      <tr><td class="years">10+</td><td class="rate">$250.00 - $350.00</td></tr>
    </table>
    <table class="staff-table" style="top:146px">
      <tr><th></th><th>Rate</th></tr>
      <tr><td class="role">Law Clerks</td><td class="rate">$50.00 - $100.00</td></tr>
      <tr><td class="role">Paralegals</td><td class="rate">$75.00 - $150.00</td></tr>
      <tr><td class="role">Legal Assistants</td><td class="rate">$50.00 - $125.00</td></tr>
    </table>

    <div class="fee-section" style="top:292px">
      <h2 class="fee-section__title fee-section__title--gold">Acquisition and Divestiture ("A&amp;D") / Merger and Acquisition ("M&amp;A"),<br>Transactions, Litigation, Intellectual Property, Entity, or Estate Matters</h2>
      <p class="fee-section__sub" style="margin-top:10px">Attorneys (based on years of experience)</p>
    </div>
    <table class="rate-table" style="left:43px;top:339px">
      <tr><th>Years of Experience</th><th>Rate</th></tr>
      <tr><td class="years">0-1</td><td class="rate">$160.00 - $175.00</td></tr>
      <tr><td class="years">1-2</td><td class="rate">$175.00 - $200.00</td></tr>
      <tr><td class="years">2-3</td><td class="rate">$200.00 - $250.00</td></tr>
      <tr><td class="years">3-5</td><td class="rate">$225.00 - $250.00</td></tr>
      <tr><td class="years">5-7</td><td class="rate">$250.00 - $275.00</td></tr>
      <tr><td class="years">7-10</td><td class="rate">$275.00 - $300.00</td></tr>
      <tr><td class="years">10+</td><td class="rate">$300.00 - $500.00</td></tr>
    </table>
    <table class="staff-table" style="top:339px">
      <tr><th></th><th>Rate</th></tr>
      <tr><td class="role">Law Clerks</td><td class="rate">$50.00 - $125.00</td></tr>
      <tr><td class="role">Paralegals</td><td class="rate">$100.00 - $150.00</td></tr>
      <tr><td class="role">Legal Assistants</td><td class="rate">$50.00 - $125.00</td></tr>
    </table>
    <p class="footnote">* The firm's hourly rates are reviewed annually and<br>may change effective January 1<sup>st</sup>, unless otherwise agreed</p>
  </article>
</section>

<section class="spread spread--team">
  <article class="page page--left">
    <div class="library-backdrop" role="img" aria-label="Softly blurred shelf of law books"></div>
    <div class="profile" style="top:39px">
      <div class="profile__photo profile__photo--portrait" role="img" aria-label="Black and white portrait of attorney in suit"></div>
      <header class="profile__head">
        <p class="profile__name">Bennett A. Carrow,</p>
        <p class="profile__title">J.D., Senior Attorney, Business &amp; Litigation</p>
        <p class="profile__contact">E : bcarrow@prv.law &nbsp;(713) 555-0142 x116</p>
      </header>
      <div class="profile__bio">
        <p>Bennett A. Carrow is a Senior Attorney with Pierce, Ravel &amp; Vance, PLLC. Bennett's practice focuses on commercial litigation, business law, and general corporate transactions. He is an alumnus of Pine Ridge State University and received his Juris Doctorate from Bayou State College of Law in 2012.</p>
        <p>Mr. Carrow's focused interests include commercial transactions, contract negotiating, drafting, and enforcement, litigation and motion practice, corporate structuring, maintenance, and governance, alternative dispute resolution, and trademark procurement and enforcement. Mr. Carrow clerked for the 165th Civil Judicial District Court of Harris County while attending law school, where he observed the increasing reliance that Texas courts placed on alternative dispute resolution. Accordingly, Mr. Carrow studied alternative dispute resolution and satisfied all the requirements to become a Certified Texas Mediator. Having resolved and participated in dozens of mediations, Mr. Carrow continues to balance his experience in litigation, advocacy, and corporate transactions with the practicality and efficiency offered by the various venues of alternative dispute resolution.</p>
        <p>Mr. Carrow's experience includes a wide range of litigation and motion practice, corporate transactions, including negotiating and drafting, the complete structuring, implementation, and governance of corporate entities, intellectual property protection, defense, and enforcement, several areas of Texas family law practice, and mediating and arbitrating private and corporate disputes of all natures. This experience provides Mr. Carrow with the comprehensive ability to represent corporate and individual clients in a multitude of personal and business matters from beginning to end, whether that be the initiation of litigation to final judgment or resolution or the negotiation and memorialization of informal business proposals to the completion, execution, and satisfaction of complex transactional agreements. This experience further provides Mr. Carrow with the ability to structure and govern all types of corporate entities, including designing and implementing various taxation and asset-protection structures, from single-member LLCs designed to hold business or personal assets to multi-shareholder for-profit corporations with several commercially-available products seeking to commence its IPO.</p>
        <p>Mr. Carrow practices in the Houston, Texas, office of Pierce, Ravel &amp; Vance, PLLC.</p>
      </div>
      <div class="admissions" style="padding-top:4px">
        <p class="admissions__title">ADMISSIONS TO PRACTICE</p>
        <ul><li>Texas</li><li>U.S. Northern, Eastern, and Southern Districts of Texas</li></ul>
      </div>
    </div>
    <p class="firm-name">PR&amp;V</p>
  </article>

  <article class="page page--right">
    <div class="library-backdrop" role="img" aria-label="Softly blurred shelf of law books"></div>
    <div class="profile" style="top:39px;left:32px">
      <div class="profile__photo" role="img" aria-label="Attorney portrait placeholder"></div>
      <header class="profile__head">
        <p class="profile__name">Jared M. Holt,</p>
        <p class="profile__title">J.D., Business, Insurance &amp; Litigation Attorney</p>
        <p class="profile__contact">E : jholt@prv.law &nbsp;(713) 555-0142 x104</p>
      </header>
      <div class="profile__bio">
        <p>Jared M. Holt is an attorney at Pierce, Ravel &amp; Vance, PLLC. Jared's practice focuses on commercial litigation, business disputes, construction, residential and commercial property law, commercial transactions, and general litigation. Jared's practice includes resolving business issues such as insurance disputes, collections, corporate structuring, business dissolution, and litigation.</p>
        <p>Jared has served as lead trial counsel for litigation claims against a Gulf Coast municipality, a law firm, and attorney resulting in the successful bench verdict of $450,000. Mr. Holt has also served as counsel for temporary and permanent injunctions related to intellectual property infringement, online business disparagement, and partnership disputes. Also, Mr. Holt has individually litigated hundreds of cases to settlement and prepared dozens of cases for trial. While in law school, Jared served as the Editor-in-Chief of the International Trade Law Journal at Bayou State College of Law.</p>
        <p>Jared is admitted to practice before the United States District Courts for the Northern, Eastern, Southern, and Western Districts of Texas, all State Courts of Texas, and all State Courts of Florida. He is based in the Houston, Texas, office of Pierce, Ravel &amp; Vance, PLLC.</p>
      </div>
      <div class="admissions" style="padding-top:2px">
        <p class="admissions__title">ADMISSIONS TO PRACTICE</p>
        <ul><li>Texas</li><li>Florida</li><li>U.S. Northern, Eastern, Southern &amp; Western Districts of Texas</li></ul>
      </div>
    </div>
  </article>
</section>

</body>
</html>
```